Business Card for By Karel Voss

Looking to have a business card designed for my lifestyle and fitness company. My company offers personal training, online programming and nutrition advice based out of London, United Kingdom.

I'd like to see modern, sleek designs, focusing on black, matte black or matte grey. Design doesn't need to be overly descriptive as this will also be used as a personal business card. I've included my logo.

Please note that my company is no longer called "Fitness by Karel Voss" but instead "By Karel Voss", this is because of my other ventures. Therefore please don't use the "fitness by karel voss" text.

information about my company can be found at www.bykarelvoss.com

Company is also based out of London (United Kingdom) & Sydney (Australia) this could be reflected on the card.

Industry/Entity Type

Business

Contact Information for Business Card

Karel Voss
+44 7382 615027
karel@bykarelvoss.com
www.bykarelvoss.com

Font styles to use
Sans Serif

Requirements
Must have
• All contact details and inclusion of my logo.

```html
<!DOCTYPE html>
<html lang="en">
<head>
<meta charset="utf-8">
<title>By Karel Voss – Business Card</title>
<link rel="stylesheet" href="https://fonts.googleapis.com/css2?family=Raleway:wght@300;600&family=Arimo&family=Tinos&display=swap">
<style>
  :root {
    --black: #000000;
    --card: #0a0a0a;
    --silver: #a8a8a8;
    --text-light: #cfcfcf;
    --ghost: #1c1c1c;
    --stage-light: #c9c9c9;
    --stage-dark: #6e6e6e;
  }
  * { margin: 0; padding: 0; box-sizing: border-box; }
  html, body { width: 674px; height: 1200px; overflow: hidden; background: var(--black); }
  .canvas { position: relative; width: 674px; height: 1200px; }

  /* Front of card */
  .card-front {
    position: absolute; left: 0; top: 0; width: 674px; height: 385px;
    background: var(--black);
    display: flex; flex-direction: column; align-items: center; justify-content: center; gap: 22px;
  }
  .brand-dot { width: 56px; height: 56px; border-radius: 50%; background: var(--silver); }
  .brand-name {
    font-family: "Raleway", sans-serif; font-weight: 600;
    font-size: 38px; letter-spacing: 3px; text-transform: uppercase; color: var(--silver);
  }

  /* Presentation band with both faces laid flat */
  .stage {
    position: absolute; left: 0; top: 385px; width: 674px; height: 429px;
    background: radial-gradient(ellipse at 50% 40%, var(--stage-light), var(--stage-dark));
  }
  .mini {
    position: absolute; width: 250px; height: 143px; background: var(--card);
    box-shadow: 0 8px 18px rgba(0,0,0,.35); overflow: hidden;
  }
  .mini-front { left: 72px; top: 58px; display: flex; flex-direction: column; align-items: center; justify-content: center; gap: 9px; }
  .mini-front .brand-dot { width: 20px; height: 20px; }
  .mini-front .brand-name { font-size: 14px; letter-spacing: 1px; }
  .mini-back { left: 352px; top: 228px; }
  .mini-back .person-name { left: 16px; top: 20px; font-size: 16px; padding-left: 8px; border-left-width: 1px; }
  .mini-back .contact-list { left: 16px; top: 92px; gap: 3px; }
  .mini-back .contact-list li { font-size: 8px; padding-left: 7px; border-left-width: 1px; }
  .mini-back .ghost-name { font-size: 34px; right: -10px; top: 10px; }

  /* Back of card */
  .card-back {
    position: absolute; left: 0; top: 814px; width: 674px; height: 386px;
    background: var(--black); overflow: hidden;
  }
  .ghost-name {
    position: absolute; right: -20px; top: 30px; text-align: right;
    font-family: "Raleway", sans-serif; font-weight: 600; text-transform: uppercase;
    font-size: 84px; line-height: 1; color: var(--ghost);
  }
  .person-name {
    position: absolute; left: 42px; top: 60px;
    padding-left: 22px; border-left: 2px solid var(--text-light);
    font-family: "Raleway", sans-serif; font-weight: 300; text-transform: uppercase;
    font-size: 45px; line-height: 1.22; letter-spacing: 7px; color: var(--text-light);
  }
  .contact-list {
    position: absolute; left: 42px; top: 256px; list-style: none;
    display: flex; flex-direction: column; gap: 9px;
  }
  .contact-list li {
    padding-left: 22px; border-left: 3px solid var(--text-light);
    font-family: "Arimo", sans-serif; font-size: 18px; line-height: 1.2; color: var(--text-light);
  }
  .contact-list .phone { font-family: "Tinos", serif; font-size: 21px; letter-spacing: 2px; }
</style>
</head>
<body>
<div class="canvas">

  <section class="card-front">
    <span class="brand-dot"></span>
    <span class="brand-name">By Karel Voss</span>
  </section>

  <section class="stage">
    <div class="mini mini-front">
      <span class="brand-dot"></span>
      <span class="brand-name">By Karel Voss</span>
    </div>
    <div class="mini mini-back">
      <span class="ghost-name">By Karel<br>Voss</span>
      <h2 class="person-name">Karel<br>Voss</h2>
      <ul class="contact-list">
        <li class="phone">+44 7382 615027</li>
        <li>www.bykarelvoss.com</li>
        <li>karel@bykarelvoss.com</li>
      </ul>
    </div>
  </section>

  <section class="card-back">
    <span class="ghost-name">By Karel<br>Voss</span>
    <h1 class="person-name">Karel<br>Voss</h1>
    <ul class="contact-list">
      <li class="phone">+44 7382 615027</li>
      <li>www.bykarelvoss.com</li>
      <li>karel@bykarelvoss.com</li>
    </ul>
  </section>

</div>
</body>
</html>
```